Tractor Trailer & Van Graphics

Develop Graphics for our Vans, Tractor & Trailers, See our website www.quinleyforge.com for brand theme, I included a Brand Style Guide.
On the back doors of the trucks and van we want to highlight our core products, Packaging, Displays, Protective & E commerce, we are very proud of our sustainability efforts as we are 100% solar powered

Target Market(s)

Create Brand identify

Requirements
Must have
• Follow our brand guide line
Nice to have
• Logo. Locations Bullet point on back of trailer
Show Back door options
Show logo on tractor only
trailer show full. 1/2 coverage
Van full wrap

```html
<!DOCTYPE html>
<html lang="en">
<head>
<meta charset="utf-8">
<title>Quinleyforge Packaging – Van Side Wrap</title>
<link href="https://fonts.googleapis.com/css2?family=Michroma&family=Alfa+Slab+One&display=swap" rel="stylesheet">
<style>
  :root {
    --panel-white: #f6f6f6;
    --panel-shade: #ececec;
    --brand-orange: #df4f16;
    --band-orange: #dc6a2a;
    --band-deep: #c9551a;
    --glow: #fff8ee;
    --type-grey: #777777;
    --ink: #1a1a1a;
    --trim: #ffffff;
  }
  * { box-sizing: border-box; margin: 0; padding: 0; }
  html, body {
    width: 1200px;
    height: 778px;
    overflow: hidden;
    background: #ffffff;
  }
  .wrap-panel {
    position: relative;
    width: 1200px;
    height: 778px;
    background: linear-gradient(180deg, var(--panel-white) 0%, var(--panel-shade) 100%);
    overflow: hidden;
  }
  .brand-lockup {
    position: absolute;
    left: 170px;
    top: 150px;
    display: flex;
    align-items: center;
    gap: 40px;
  }
  .brand-mark {
    width: 128px;
    height: 128px;
    background: var(--brand-orange);
    flex: none;
  }
  .brand-text { display: flex; flex-direction: column; }
  .brand-name {
    font-family: "Michroma", sans-serif;
    font-weight: 400;
    font-size: 60px;
    line-height: 1;
    color: var(--brand-orange);
    letter-spacing: 0;
    white-space: nowrap;
  }
  .brand-descriptor {
    font-family: "Michroma", sans-serif;
    font-size: 24px;
    line-height: 1;
    color: var(--type-grey);
    letter-spacing: 34px;
    margin-top: 26px;
    margin-left: 130px;
    white-space: nowrap;
  }
  .color-band {
    position: absolute;
    left: 0;
    top: 400px;
    width: 1200px;
    height: 378px;
    background: linear-gradient(180deg, var(--band-orange) 0%, var(--band-deep) 100%);
  }
  .sunburst {
    position: absolute;
    inset: 0;
    background: radial-gradient(ellipse 460px 340px at 56% 4%, var(--glow) 0%, rgba(255,232,210,0.75) 18%, rgba(255,205,165,0.3) 50%, rgba(255,200,160,0) 100%);
  }
  .web-address {
    position: absolute;
    left: 0;
    right: 0;
    top: 118px;
    text-align: center;
    font-family: "Alfa Slab One", serif;
    font-size: 50px;
    line-height: 1;
    color: var(--ink);
    letter-spacing: 0;
    white-space: nowrap;
    text-shadow: 3px 0 0 var(--trim), -3px 0 0 var(--trim), 0 3px 0 var(--trim), 0 -3px 0 var(--trim),
                 2px 2px 0 var(--trim), -2px -2px 0 var(--trim), 2px -2px 0 var(--trim), -2px 2px 0 var(--trim);
  }
</style>
</head>
<body>
  <main class="wrap-panel">
    <section class="brand-lockup">
      <div class="brand-mark" aria-hidden="true"></div>
      <div class="brand-text">
        <h1 class="brand-name">QUINLEYFORGE</h1>
        <p class="brand-descriptor">PACKAGING</p>
      </div>
    </section>
    <section class="color-band">
      <div class="sunburst" role="img" aria-label="Soft radiating light burst across the orange band"></div>
      <p class="web-address">www.quinleyforge.com</p>
    </section>
  </main>
</body>
</html>
```